43 Year Old Construction firm needs Updated Business Card & Stationery Design

We are an established and well known (in our market) commercial construction firm. We need a cleaner and more modern look for our corporate identity material. We would like to continue to use our current colors and logo.
We are thinking about incorporating a slogan on our business card (either front or back): "Striving to be the most trusted builder in our market." The text could change at some point. Our website is www.kvoplarn.com . Sample card is attached. Some will have more phone numbers, etc...
Updates

Target Market(s)

Commercial and institutional clients.

Industry/Entity Type

Construction Company

Contact Information for Business Card

See attached for existing card. But don't be constrained.

Requirements
Must have
• Logo, name, title, address, website, email, phone numbers (as few as one, as many as three)
• Slogan on front or back "Striving to be the most trusted builder in our market"
• Use existing logo and colors

```html
<!DOCTYPE html>
<html lang="en">
<head>
<meta charset="utf-8">
<title>Kvoplarn Constructors – Business Card</title>
<link href="https://fonts.googleapis.com/css2?family=Noto+Serif:wght@400;700&display=swap" rel="stylesheet">
<style>
  :root {
    --stage: #2b2b2d;
    --brand-blue: #154a86;
    --brand-green: #1f9e4a;
    --paper: #ffffff;
    --ink: #1b3f73;
  }
  * { box-sizing: border-box; margin: 0; padding: 0; }
  html, body { width: 1200px; height: 900px; overflow: hidden; }
  body {
    background: var(--stage);
    font-family: "Noto Serif", Georgia, serif;
    position: relative;
  }
  .card {
    position: absolute;
    width: 560px;
    height: 320px;
    overflow: hidden;
    box-shadow: 0 14px 30px rgba(0,0,0,.45);
  }

  /* Shared brand panel */
  .brand-panel {
    position: absolute;
    display: flex;
    flex-direction: column;
    justify-content: center;
    align-items: center;
    text-align: center;
    font-weight: 700;
    line-height: 1.15;
    font-size: 30px;
  }
  .brand-panel .brand-sub { font-size: 19px; letter-spacing: 2px; }

  /* Back side */
  .card--back {
    left: 80px; top: 90px;
    background: var(--brand-blue);
    color: var(--paper);
  }
  .card--back .brand-panel {
    left: 30px; top: 64px;
    width: 290px; height: 150px;
    background: var(--paper);
    color: var(--brand-blue);
  }
  .slogan-block {
    position: absolute;
    right: 28px; bottom: 26px;
    text-align: right;
    font-size: 12.5px;
    letter-spacing: .4px;
    line-height: 1.8;
  }
  .slogan { text-transform: uppercase; }
  .site { font-size: 14px; }

  /* Front side */
  .card--front {
    left: 560px; top: 490px;
    background: var(--paper);
    color: var(--ink);
  }
  .card--front .brand-panel {
    left: 40px; top: 24px;
    width: 300px; height: 122px;
    background: var(--brand-blue);
    color: var(--paper);
  }
  .contact {
    position: absolute;
    left: 62px; right: 0; top: 156px;
  }
  .name-row {
    display: flex;
    align-items: flex-end;
  }
  .person-name {
    font-size: 22px;
    font-weight: 700;
    color: var(--ink);
    line-height: 1.15;
    white-space: nowrap;
  }
  .rule {
    flex: 1;
    height: 2px;
    margin: 0 0 6px 12px;
    background: var(--brand-blue);
  }
  .person-title { font-size: 13px; color: var(--brand-green); margin: 1px 0 5px 14px; line-height: 1.2; }
  .details { margin-left: 30px; font-size: 13px; line-height: 1.35; }
  .details li { list-style: none; display: flex; align-items: center; gap: 7px; }
  .details svg { width: 11px; height: 11px; fill: var(--brand-green); flex: none; }
</style>
</head>
<body>

<section class="card card--back" aria-label="Card back">
  <div class="brand-panel">
    <span>KVOPLARN</span>
    <span class="brand-sub">CONSTRUCTORS</span>
  </div>
  <div class="slogan-block">
    <p class="slogan">Striving to be the most trusted builder in our market</p>
    <p class="site">www.kvoplarn.com</p>
  </div>
</section>

<section class="card card--front" aria-label="Card front">
  <div class="brand-panel">
    <span>KVOPLARN</span>
    <span class="brand-sub">CONSTRUCTORS</span>
  </div>
  <div class="contact">
    <div class="name-row">
      <p class="person-name">Daniel R. Whitcombe</p>
      <div class="rule"></div>
    </div>
    <p class="person-title">President</p>
    <ul class="details">
      <li>4120 Cedarline Avenue</li>
      <li>Fairmont, MO 63150-1184</li>
      <li>
        <svg viewBox="0 0 24 24"><path d="M6.6 10.8a15.1 15.1 0 0 0 6.6 6.6l2.2-2.2a1 1 0 0 1 1-.25 11.4 11.4 0 0 0 3.6.57 1 1 0 0 1 1 1V20a1 1 0 0 1-1 1A17 17 0 0 1 3 4a1 1 0 0 1 1-1h3.5a1 1 0 0 1 1 1c0 1.25.2 2.45.57 3.57a1 1 0 0 1-.25 1z"/></svg>
        Direct 314-555-0187
      </li>
      <li>
        <svg viewBox="0 0 24 24"><path d="M2 5h20v14H2zm2 2v.5l8 5 8-5V7zm0 2.8V17h16V9.8l-8 5z"/></svg>
        dwhit@kvoplarn.com
      </li>
      <li>
        <svg viewBox="0 0 24 24"><circle cx="12" cy="12" r="10"/></svg>
        www.kvoplarn.com
      </li>
    </ul>
  </div>
</section>

</body>
</html>
```